We are launching in December, a range of supplements and vitamins.

We have just made an amend to the mission statement and how we are going to give back to society. Please can you add both to the packaging:

Verdant’s purpose is to support health, wellbeing and longevity, so that we can all thrive in the modern world; an environment so alien to that in which we evolved. Embracing technology, research and science, we harness nature’s goodness - enabling us all to love life – naturally.

Twice Kind Promise. For each and every Verdant supplement you take, we provide a supplement to an under nourished child.

For every supplement we sell: £1 goes to the charity ‘Little Lights Fund’ and in addition we provide one healthy meal to an under privileged child in India.

My name is Mark Holloway and I own several companies including www.quartzelle.com (you can check me out on Infopedex – I am not the football referee nor the rocket scientist, but the entrepreneur) . Over the past 2 years I have been writing a book to help people live more healthily and it launches in December. It’s called Verdant Way. While doing my research for the book, I came to realise that most supplements and vitamin products on the market are rubbish! Most are made for profit and not for the benefit of the consumer. I want to change all of that. Howard Pellow is patron of a charity I set up with my brother Paul Holloway and together we have built 11 schools in Asia. I am hoping to get Howards help in getting my supplements to market.

Positioning of our supplements - In a world where so much has changed from the one our bodies were designed to thrive, at Verdant Supplements we are driven by one purpose; to globally provide healthy support to life in the 21st century. While the roots of our wellbeing supplements date back beyond 10,000BC, we embrace modern technology and science, to encapsulate powerful phytonutrients, herbs and other goodness. The essence of which is to promote health, happiness and longevity.

So what are we looking for in the design? Something that stands out. Something that looks professional. A design and concept that can role out across 24 different products. Some products are simple, just one ingredient, such as vitamin D3, Magnesium, Garlic Extracts etc, and others are our own formulas where there are up to 30 different ingredients. You can contact me at any time with questions at Mark@verdantway-example.com

Target Market(s)

Male & Female 20 years plus, mainly UK

Industry/Entity Type

Medical

Logo Text

VERDANT - Sub heading = Thriving Days Gently

Colors

Designer to choose colors to be used in the design.

Requirements
Must have
• see attached powerpoint.
• We have just made an amend to the mission statement and how we are going to give back to society. Please can you add both to the packaging:
• Verdant’s purpose is to support health, wellbeing and longevity, so that we can all thrive in the modern world; an environment so alien to that in which we evolved. Embracing technology, research and science, we harness nature’s goodness - enabling us all to love life – naturally.
• Twice Kind Promise. For each and every Verdant supplement you take, we provide a supplement to an under nourished child.
Nice to have
• see attached powerpoint
Should not have
• see attached powerpoint

```html
<!DOCTYPE html>
<html lang="en">
<head>
<meta charset="utf-8">
<title>Verdant Way — Supplement Labels</title>
<link rel="stylesheet" href="https://fonts.googleapis.com/css2?family=Oswald:wght@500;700&family=Roboto+Condensed:wght@400;700&family=Courier+Prime&family=Libre+Baskerville:ital@1&display=swap">
<style>
  :root {
    --page: #ececec;
    --paper: #fbfbfa;
    --ink: #1c1c1c;
    --sleep: #29a6e3;
    --vitamin: #eaa312;
    --energy: #d1252e;
    --greentea: #2dc774;
    --rule: #1c1c1c;
  }
  * { box-sizing: border-box; margin: 0; padding: 0; }
  html, body {
    width: 1200px; height: 900px; overflow: hidden;
    background: var(--page);
  }
  .range {
    width: 1200px; height: 900px;
    display: flex; justify-content: center; align-items: center; gap: 20px;
  }
  .label {
    width: 275px; height: 462px;
    background: var(--paper);
    display: flex; flex-direction: column;
    box-shadow: 0 2px 6px rgba(0,0,0,0.12);
  }
  .label--sleep { --accent: var(--sleep); }
  .label--vitamin { --accent: var(--vitamin); }
  .label--energy { --accent: var(--energy); }
  .label--greentea { --accent: var(--greentea); }

  .brand-area {
    height: 186px; position: relative;
    display: flex; flex-direction: column; align-items: center;
    padding-top: 46px;
  }
  .established {
    position: absolute; top: 22px; left: 22px; right: 22px;
    display: flex; justify-content: space-between;
    font-family: "Roboto Condensed", sans-serif; font-weight: 700;
    font-size: 8px; color: var(--ink);
  }
  .established .est { letter-spacing: 5px; font-weight: 400; }
  .brand-name {
    font-family: "Oswald", sans-serif; font-weight: 700;
    color: var(--accent); text-align: center; line-height: 0.95;
    text-transform: uppercase;
  }
  .brand-name .first { display: block; font-size: 44px; letter-spacing: 1px; }
  .brand-name .second { display: block; font-size: 58px; letter-spacing: 2px; }
  .tagline {
    margin-top: 8px; padding-top: 3px;
    border-top: 2px solid var(--rule);
    font-family: "Oswald", sans-serif; font-weight: 500;
    font-size: 10px; letter-spacing: 2.2px; color: var(--ink);
    text-transform: uppercase;
  }

  .product-panel {
    flex: 1; background: var(--accent); color: var(--ink);
    display: flex; flex-direction: column; align-items: center;
    padding: 22px 22px 0;
  }
  .product-name {
    font-family: "Oswald", sans-serif; font-weight: 700;
    font-size: 48px; line-height: 1; letter-spacing: 1px;
    text-transform: uppercase; white-space: nowrap;
  }
  .product-name sup { font-size: 26px; vertical-align: 18px; }
  .product-type {
    margin-top: 6px;
    font-family: "Courier Prime", monospace; font-size: 15px;
    letter-spacing: 6px; text-transform: uppercase;
  }
  .rule { width: 100%; height: 2px; background: var(--rule); }
  .rule--short { width: 82%; margin-top: 8px; }
  .dosage {
    width: 82%; display: flex; align-items: center; justify-content: space-between;
    padding: 7px 14px 6px 6px;
  }
  .dosage .count {
    display: flex; align-items: center; gap: 3px;
    font-family: "Libre Baskerville", serif; font-size: 14px;
  }
  .dosage .divider { width: 2px; height: 20px; background: var(--rule); }
  .dosage .weight {
    font-family: "Libre Baskerville", serif; font-style: italic; font-size: 14px;
  }
  .statement {
    margin-top: 12px;
    font-family: "Roboto Condensed", sans-serif; font-size: 9.6px;
    line-height: 1.5; text-align: justify; width: 100%;
  }
  .statement strong { font-weight: 700; text-transform: uppercase; }
  .statement + .rule { margin-top: 6px; }
  .rule + .statement { margin-top: 6px; }
  .product-panel > .rule:last-child { margin-top: 6px; }
</style>
</head>
<body>
<main class="range">

  <article class="label label--sleep">
    <header class="brand-area">
      <div class="established"><span class="est">EST.</span><span>10,000 BC</span></div>
      <div class="brand-name"><span class="first">Verdant</span><span class="second">Way</span></div>
      <div class="tagline">Thriving Days Gently</div>
    </header>
    <section class="product-panel">
      <h2 class="product-name">Sleep</h2>
      <p class="product-type">Supplement</p>
      <div class="rule rule--short"></div>
      <div class="dosage">
        <span class="count"><svg width="20" height="12" viewBox="0 0 20 12" aria-hidden="true"><ellipse cx="10" cy="6" rx="8.5" ry="4.8" fill="none" stroke="#1c1c1c" stroke-width="1.6"/><line x1="2" y1="6" x2="18" y2="6" stroke="#1c1c1c" stroke-width="1.6"/></svg>× 30</span>
        <span class="divider"></span>
        <span class="weight">1125mg</span>
      </div>
      <div class="rule"></div>
      <p class="statement"><strong>Verdant’s purpose</strong> is to support health, wellbeing and longevity, so that we can all thrive in the modern world; an environment so alien to that in which we evolved. Embracing technology, research and science, we harness nature’s goodness - enabling us all to love life – naturally.</p>
      <div class="rule"></div>
      <p class="statement"><strong>Twice Kind Promise:</strong> For each and every Verdant supplement you take, we provide a supplement to an under nourished child.</p>
      <div class="rule"></div>
    </section>
  </article>

  <article class="label label--vitamin">
    <header class="brand-area">
      <div class="established"><span class="est">EST.</span><span>10,000 BC</span></div>
      <div class="brand-name"><span class="first">Verdant</span><span class="second">Way</span></div>
      <div class="tagline">Thriving Days Gently</div>
    </header>
    <section class="product-panel">
      <h2 class="product-name">Vitamin D<sup>3</sup></h2>
      <p class="product-type">Supplement</p>
      <div class="rule rule--short"></div>
      <div class="dosage">
        <span class="count"><svg width="20" height="12" viewBox="0 0 20 12" aria-hidden="true"><ellipse cx="10" cy="6" rx="8.5" ry="4.8" fill="none" stroke="#1c1c1c" stroke-width="1.6"/><line x1="2" y1="6" x2="18" y2="6" stroke="#1c1c1c" stroke-width="1.6"/></svg>× 30</span>
        <span class="divider"></span>
        <span class="weight">1125mg</span>
      </div>
      <div class="rule"></div>
      <p class="statement"><strong>Verdant’s purpose</strong> is to support health, wellbeing and longevity, so that we can all thrive in the modern world; an environment so alien to that in which we evolved. Embracing technology, research and science, we harness nature’s goodness - enabling us all to love life – naturally.</p>
      <div class="rule"></div>
      <p class="statement"><strong>Twice Kind Promise:</strong> For each and every Verdant supplement you take, we provide a supplement to an under nourished child.</p>
      <div class="rule"></div>
    </section>
  </article>

  <article class="label label--energy">
    <header class="brand-area">
      <div class="established"><span class="est">EST.</span><span>10,000 BC</span></div>
      <div class="brand-name"><span class="first">Verdant</span><span class="second">Way</span></div>
      <div class="tagline">Thriving Days Gently</div>
    </header>
    <section class="product-panel">
      <h2 class="product-name">Energy</h2>
      <p class="product-type">Supplement</p>
      <div class="rule rule--short"></div>
      <div class="dosage">
        <span class="count"><svg width="20" height="12" viewBox="0 0 20 12" aria-hidden="true"><ellipse cx="10" cy="6" rx="8.5" ry="4.8" fill="none" stroke="#1c1c1c" stroke-width="1.6"/><line x1="2" y1="6" x2="18" y2="6" stroke="#1c1c1c" stroke-width="1.6"/></svg>× 30</span>
        <span class="divider"></span>
        <span class="weight">1125mg</span>
      </div>
      <div class="rule"></div>
      <p class="statement"><strong>Verdant’s purpose</strong> is to support health, wellbeing and longevity, so that we can all thrive in the modern world; an environment so alien to that in which we evolved. Embracing technology, research and science, we harness nature’s goodness - enabling us all to love life – naturally.</p>
      <div class="rule"></div>
      <p class="statement"><strong>Twice Kind Promise:</strong> For each and every Verdant supplement you take, we provide a supplement to an under nourished child.</p>
      <div class="rule"></div>
    </section>
  </article>

  <article class="label label--greentea">
    <header class="brand-area">
      <div class="established"><span class="est">EST.</span><span>10,000 BC</span></div>
      <div class="brand-name"><span class="first">Verdant</span><span class="second">Way</span></div>
      <div class="tagline">Thriving Days Gently</div>
    </header>
    <section class="product-panel">
      <h2 class="product-name">Green Tea</h2>
      <p class="product-type">Extract</p>
      <div class="rule rule--short"></div>
      <div class="dosage">
        <span class="count"><svg width="20" height="12" viewBox="0 0 20 12" aria-hidden="true"><ellipse cx="10" cy="6" rx="8.5" ry="4.8" fill="none" stroke="#1c1c1c" stroke-width="1.6"/><line x1="2" y1="6" x2="18" y2="6" stroke="#1c1c1c" stroke-width="1.6"/></svg>× 30</span>
        <span class="divider"></span>
        <span class="weight">1125mg</span>
      </div>
      <div class="rule"></div>
      <p class="statement"><strong>Verdant’s purpose</strong> is to support health, wellbeing and longevity, so that we can all thrive in the modern world; an environment so alien to that in which we evolved. Embracing technology, research and science, we harness nature’s goodness - enabling us all to love life – naturally.</p>
      <div class="rule"></div>
      <p class="statement"><strong>Twice Kind Promise:</strong> For each and every Verdant supplement you take, we provide a supplement to an under nourished child.</p>
      <div class="rule"></div>
    </section>
  </article>

</main>
</body>
</html>
```